Simple, Professional and neat business card design for Vendralo Inc.

We're looking to re-vamp our business card design. We're a supplier of innovative feed ingredients for the North American animal agriculture industry. We are located in Halverton, Norland County and our flagship product is a product that prevents milk fever in dairy cows when the calve, it is fed before calving and is very effective compared to other alternatives available on the market today.

Our company has Danish roots and we import all of our product from our Danish partner/manufacturer in Denmark. We like our design to embrace high professionalism while remaining neat and simple.

Target Market(s)

B2B, Feed Mills, Veterinary Clinics, Large integrators/producers,

Industry/Entity Type

Agribusiness

Contact Information for Business Card

We like the rounded corners because they make the card easy to sit in a wallet and not many use it so it makes the card stand out, just possibly something to take account for during the design.

As you can also see on the sliders below, looking for a that simple but proffesional scandinavian design.

Requirements
Nice to have
• Rounded corners
Should not have
• Too vibrant

```html
<!DOCTYPE html>
<html lang="en">
<head>
<meta charset="utf-8">
<title>Vendralo Inc. – Business Card</title>
<link rel="stylesheet" href="https://fonts.googleapis.com/css2?family=Open+Sans:wght@400;600;700&display=swap">
<style>
  :root {
    --backdrop: #2a2d31;
    --blue: #1d5fb4;
    --white: #ffffff;
    --paper-shade: #eceef1;
    --ink: #2b2b2b;
    --gold-light: #ecd39d;
    --gold: #d9b872;
  }
  * { box-sizing: border-box; margin: 0; padding: 0; }
  html, body {
    width: 1200px; height: 900px; overflow: hidden;
    background: var(--backdrop);
    font-family: "Open Sans", Arial, sans-serif;
  }
  .canvas {
    width: 1200px; height: 900px;
    display: flex; flex-direction: column;
    align-items: center; justify-content: center; gap: 60px;
  }
  .card {
    position: relative;
    width: 560px; height: 320px;
    border-radius: 28px;
    overflow: hidden;
  }
  .card__band {
    position: absolute; left: 0; right: 0; bottom: 0;
    height: 26px; background: var(--blue);
  }

  /* Front */
  .card--front { background: var(--white); }
  .front__rays {
    position: absolute; inset: 0;
    background: radial-gradient(circle at 55% 55%, var(--white) 0%, var(--paper-shade) 70%);
  }
  .name-tab {
    position: absolute; left: 0; top: 34px;
    width: 280px; height: 60px;
    background: var(--blue);
    color: var(--white);
    padding: 8px 0 0 40px;
  }
  .name-tab__name { font-size: 22px; font-weight: 700; line-height: 1.15; white-space: nowrap; }
  .name-tab__title { font-size: 12px; font-weight: 400; }
  .phones {
    position: absolute; left: 40px; top: 118px;
    font-size: 15px; line-height: 1.45; color: var(--ink);
  }
  .phones__group + .phones__group { margin-top: 10px; }
  .phones__label { color: var(--blue); }
  .brand {
    position: absolute; left: 290px; top: 70px;
    display: flex; align-items: center; gap: 10px;
    white-space: nowrap;
  }
  .brand__dot {
    flex: none;
    width: 34px; height: 34px; border-radius: 50%;
    background: var(--blue);
  }
  .brand__name {
    font-size: 26px; font-weight: 700; color: var(--blue);
    letter-spacing: 0.3px; white-space: nowrap;
  }
  .contact {
    position: absolute; left: 334px; top: 150px;
    font-size: 15px; line-height: 1.45; color: var(--ink);
  }
  .contact__address { margin-bottom: 10px; }
  .contact__web { font-weight: 700; }

  /* Back */
  .card--back { background: linear-gradient(160deg, var(--gold-light), var(--gold)); }
  .back__rays {
    position: absolute; inset: 0;
    background: radial-gradient(circle at 50% 42%, rgba(255,255,255,0.45) 0%, rgba(255,255,255,0) 55%);
  }
  .back__brand {
    position: absolute; left: 0; right: 0; top: 110px;
    display: flex; justify-content: center; align-items: center; gap: 12px;
    white-space: nowrap;
  }
  .back__brand .brand__dot { width: 44px; height: 44px; }
  .back__brand .brand__name { font-size: 34px; }
  .social {
    position: absolute; left: 0; right: 0; top: 210px;
    display: flex; justify-content: center; gap: 14px;
  }
  .social__dot {
    width: 26px; height: 26px; border-radius: 50%;
    background: var(--blue);
  }
</style>
</head>
<body>
<main class="canvas">

  <section class="card card--front">
    <div class="front__rays" role="img" aria-label="Faint light sunburst rays behind the brand emblem"></div>
    <div class="name-tab">
      <div class="name-tab__name">Henrik Solberg</div>
      <div class="name-tab__title">Director</div>
    </div>
    <div class="phones">
      <div class="phones__group">
        <div><span class="phones__label">M:</span> 555 214 0187</div>
        <div><span class="phones__label">O:</span> 555 310 4426</div>
      </div>
      <div class="phones__group">
        <div><span class="phones__label">Toll Free:</span> 800 555 0142</div>
        <div><span class="phones__label">Fax:</span> 555 310 4490</div>
      </div>
    </div>
    <div class="brand">
      <span class="brand__dot"></span>
      <span class="brand__name">VENDRALO INC.</span>
    </div>
    <div class="contact">
      <div class="contact__address">Box 274, Halverton<br>Norland County</div>
      <div>henrik@vendralo.com</div>
      <div class="contact__web">www.vendralo.com</div>
    </div>
    <div class="card__band"></div>
  </section>

  <section class="card card--back">
    <div class="back__rays" role="img" aria-label="Soft golden sunburst rays radiating from the brand emblem"></div>
    <div class="back__brand">
      <span class="brand__dot"></span>
      <span class="brand__name">VENDRALO INC.</span>
    </div>
    <div class="social" aria-label="Social media links">
      <span class="social__dot"></span>
      <span class="social__dot"></span>
    </div>
    <div class="card__band"></div>
  </section>

</main>
</body>
</html>
```